Need a webinar banner promo to place on social media

We are organise a series of webinars in coming months.

We need a webinar banner design to be posted on Facebook and linkedin. The banner is for our webinar titled: Steps to Unveil your venture with poise and polish.

our website is www.bravolinhub.com.au

there is a link on the website to the webinar registration for your reference.

```html
<!DOCTYPE html>
<html lang="en">
<head>
<meta charset="utf-8">
<title>Bravolin Hub – Webinar Banners</title>
<link rel="stylesheet" href="https://fonts.googleapis.com/css2?family=Bebas+Neue&family=Oswald:wght@200;300;500&family=Montserrat:wght@500;600;700&display=swap">
<style>
  :root{
    --board:#c8c8c8;
    --navy:#0e1838;
    --navy-mid:#17244f;
    --navy-light:#1f2f63;
    --gold-a:#f4cf3c;
    --gold-b:#fff0a6;
    --gold-c:#c99a1e;
    --white:#ffffff;
    --ink:#101424;
    --gold-grad:linear-gradient(100deg,var(--gold-a) 0%,var(--gold-b) 45%,var(--gold-c) 75%,var(--gold-a) 100%);
  }
  *{margin:0;padding:0;box-sizing:border-box}
  html,body{width:1200px;height:803px;overflow:hidden;background:var(--board)}
  .board{position:relative;width:1200px;height:803px}

  .banner{position:absolute;overflow:hidden;background:var(--navy);box-shadow:6px 6px 8px rgba(0,0,0,.35)}
  .banner > *{position:absolute}
  .banner .photo{inset:0;background:
      radial-gradient(ellipse at 30% 40%,var(--navy-light) 0%,transparent 60%),
      radial-gradient(ellipse at 75% 75%,var(--navy-mid) 0%,transparent 55%),
      linear-gradient(180deg,var(--navy-mid),var(--navy));opacity:.9}

  .gold{background:var(--gold-grad);-webkit-background-clip:text;background-clip:text;color:transparent}
  .headline{font-family:"Bebas Neue",sans-serif;line-height:.92;white-space:nowrap}
  .subline{font-family:"Montserrat",sans-serif;font-weight:600;color:var(--white);white-space:nowrap;
           border-top:1.5px solid var(--gold-a);border-bottom:1.5px solid var(--gold-a);display:flex;align-items:center;justify-content:center}
  .expo{font-family:"Bebas Neue",sans-serif;white-space:nowrap;line-height:1}
  .expo .light{font-family:"Oswald",sans-serif;font-weight:300;color:var(--white);font-size:.88em}
  .day{font-family:"Bebas Neue",sans-serif;line-height:1}
  .month{font-family:"Bebas Neue",sans-serif;color:var(--white);line-height:1}
  .year{font-family:"Bebas Neue",sans-serif;color:var(--ink);background:var(--gold-grad);letter-spacing:.12em;display:flex;align-items:center;justify-content:center;line-height:1}
  .time{font-family:"Oswald",sans-serif;font-weight:200;color:var(--white);line-height:1;white-space:nowrap}
  .register{font-family:"Bebas Neue",sans-serif;color:var(--ink);background:var(--gold-grad);display:flex;align-items:center;justify-content:center;line-height:1}
  .url{font-family:"Montserrat",sans-serif;font-weight:700;color:var(--ink);background:var(--white);display:flex;align-items:center;justify-content:center;white-space:nowrap}
  .brand{font-family:"Montserrat",sans-serif;font-weight:700;color:var(--white);display:flex;align-items:center;gap:5px;white-space:nowrap}
  .brand .mark{width:.7em;height:.7em;background:var(--gold-a)}

  /* Square post */
  .square{left:79px;top:149px;width:397px;height:494px}
  .square .brand{left:0;right:0;top:52px;justify-content:center;font-size:22px}
  .square .headline{left:0;right:0;top:146px;text-align:center;font-size:52px}
  .square .subline{left:56px;top:250px;width:281px;height:28px;font-size:15px;letter-spacing:.16em}
  .square .expo{left:89px;top:303px;font-size:21px}
  .square .day{left:87px;top:326px;font-size:86px}
  .square .month{left:156px;top:328px;font-size:31px}
  .square .year{left:234px;top:329px;width:65px;height:23px;font-size:21px}
  .square .time{left:155px;top:356px;font-size:40px}
  .square .register{left:56px;top:418px;width:74px;height:23px;font-size:16px}
  .square .url{left:132px;top:418px;width:205px;height:23px;font-size:10px}

  /* Wide banner */
  .wide{left:509px;top:149px;width:614px;height:227px}
  .wide .headline{left:39px;top:18px;font-size:48px}
  .wide .subline{left:39px;top:113px;width:247px;height:37px;font-size:17px}
  .wide .expo{left:333px;top:21px;font-size:22px}
  .wide .day{left:330px;top:50px;font-size:98px}
  .wide .month{left:408px;top:52px;font-size:34px}
  .wide .year{left:499px;top:53px;width:73px;height:27px;font-size:24px}
  .wide .time{left:408px;top:82px;font-size:46px}
  .wide .register{left:334px;top:140px;width:151px;height:39px;font-size:28px}
  .wide .brand{left:494px;top:150px;font-size:13px}
  .wide .url{left:334px;top:183px;width:238px;height:22px;font-size:11.5px}

  /* Medium banner */
  .medium{left:509px;top:406px;width:538px;height:236px}
  .medium .headline{left:31px;top:23px;font-size:44px}
  .medium .subline{left:31px;top:104px;width:207px;height:33px;font-size:14.5px}
  .medium .expo{left:270px;top:26px;font-size:20px}
  .medium .day{left:268px;top:53px;font-size:94px}
  .medium .month{left:344px;top:55px;font-size:32px}
  .medium .year{left:433px;top:56px;width:72px;height:27px;font-size:24px}
  .medium .time{left:343px;top:85px;font-size:44px}
  .medium .register{left:271px;top:141px;width:148px;height:38px;font-size:27px}
  .medium .brand{left:426px;top:151px;font-size:12.5px}
  .medium .url{left:271px;top:184px;width:234px;height:25px;font-size:11.5px}
</style>
</head>
<body>
<main class="board">

  <section class="banner square">
    <div class="photo" role="img" aria-label="Dimmed navy-toned photo of a seated seminar audience"></div>
    <div class="brand"><span class="mark"></span>BRAVOLIN HUB</div>
    <h1 class="headline gold">STEPS TO UNVEIL<br>YOUR VENTURE</h1>
    <p class="subline">WITH POISE &amp; POLISH</p>
    <p class="expo"><span class="gold">BRAVOLIN VENTURE</span> <span class="light">EXPO 2023</span></p>
    <p class="day gold">15</p>
    <p class="month">MARCH</p>
    <p class="year">2023</p>
    <p class="time">7PM-8PM</p>
    <p class="register">REGISTER NOW</p>
    <p class="url">www.bravolinhub.com.au/webinars</p>
  </section>

  <section class="banner wide">
    <div class="photo" role="img" aria-label="Dimmed navy-toned photo of a seated seminar audience"></div>
    <h2 class="headline gold">STEPS TO UNVEIL<br>YOUR VENTURE</h2>
    <p class="subline">WITH POISE &amp; POLISH</p>
    <p class="expo"><span class="gold">BRAVOLIN VENTURE</span> <span class="light">EXPO 2023</span></p>
    <p class="day gold">15</p>
    <p class="month">MARCH</p>
    <p class="year">2023</p>
    <p class="time">7PM-8PM</p>
    <p class="register">REGISTER NOW</p>
    <div class="brand"><span class="mark"></span>BRAVOLIN</div>
    <p class="url">www.bravolinhub.com.au/webinars</p>
  </section>

  <section class="banner medium">
    <div class="photo" role="img" aria-label="Dimmed navy-toned photo of a seated seminar audience"></div>
    <h2 class="headline gold">STEPS TO UNVEIL<br>YOUR VENTURE</h2>
    <p class="subline">WITH POISE &amp; POLISH</p>
    <p class="expo"><span class="gold">BRAVOLIN VENTURE</span> <span class="light">EXPO 2023</span></p>
    <p class="day gold">15</p>
    <p class="month">MARCH</p>
    <p class="year">2023</p>
    <p class="time">7PM-8PM</p>
    <p class="register">REGISTER NOW</p>
    <div class="brand"><span class="mark"></span>BRAVOLIN</div>
    <p class="url">www.bravolinhub.com.au/webinars</p>
  </section>

</main>
</body>
</html>
```